WE HAND MAKE AND DECORATE BEAUTIFUL CREATIVE GINGER BREAD HOUSES FOR CHRISTMAS AND CUPCAKES FOR SPECIAL OCCASIONS

Contact Information for Business Card

PIPPIN AND MARLOW DESIGNS
ROSA 0467 213 905
MAVIS 0438104629

```html
<!DOCTYPE html>
<html lang="en">
<head>
<meta charset="utf-8">
<title>Pippin and Marlow Designs – Business Card</title>
<link rel="stylesheet" href="https://fonts.googleapis.com/css2?family=Oranienbaum&family=Dawning+of+a+New+Day&display=swap">
<style>
  :root {
    --page-bg: #f3f1ee;
    --card-top: #bfe5df;
    --card-bottom: #f6fbfa;
    --brown: #5a3d2b;
    --red: #b3282d;
    --olive: #7d8b2b;
    --tag: #e6dccd;
    --tag-text: #fbf8f2;
    --gingerbread: #d9a57a;
    --icing: #f7efe6;
  }
  * { box-sizing: border-box; margin: 0; padding: 0; }
  html, body {
    width: 1200px;
    height: 1052px;
    overflow: hidden;
    background: var(--page-bg);
  }
  .business-card {
    position: absolute;
    left: 210px;
    top: 198px;
    width: 798px;
    height: 496px;
    background: linear-gradient(180deg, var(--card-top) 0%, #dcf1ed 45%, var(--card-bottom) 100%);
    box-shadow: 0 1px 3px rgba(0,0,0,0.15);
    overflow: hidden;
  }
  .house-illustration {
    position: absolute;
    left: 250px;
    top: 16px;
    width: 332px;
    height: 236px;
    border-radius: 10px;
    background: radial-gradient(ellipse at 50% 55%, var(--gingerbread) 0%, #e6c3a2 45%, var(--icing) 75%, rgba(247,239,230,0) 100%);
  }
  .card-text {
    position: absolute;
    left: 0;
    top: 0;
    width: 798px;
    height: 496px;
  }
  .business-name { font-family: 'Oranienbaum', serif; font-size: 68px; fill: var(--brown); }
  .contact-line { font-family: 'Oranienbaum', serif; font-size: 56px; }
  .contact-rosa { fill: var(--red); }
  .contact-mavis { fill: var(--olive); }
  .find-us { font-family: 'Dawning of a New Day', cursive; font-size: 34px; fill: var(--brown); }
  .social-tags {
    position: absolute;
    left: 470px;
    top: 390px;
    display: flex;
    gap: 20px;
  }
  .social-tag {
    width: 80px;
    height: 48px;
    background: var(--tag);
    clip-path: polygon(0 0, 100% 0, 92% 50%, 100% 100%, 0 100%, 8% 50%);
    display: flex;
    align-items: center;
    justify-content: center;
    font-family: 'Oranienbaum', serif;
    font-size: 17px;
    color: var(--tag-text);
  }
</style>
</head>
<body>
  <main class="business-card">
    <div class="house-illustration" role="img" aria-label="Hand-drawn gingerbread house with iced roof, candy cane, lollipops and little trees"></div>
    <svg class="card-text" viewBox="0 0 798 496" aria-label="Contact details">
      <text class="business-name" x="50" y="308" textLength="700" lengthAdjust="spacingAndGlyphs">PIPPIN AND MARLOW DESIGNS</text>
      <text class="contact-line contact-rosa" x="50" y="371" textLength="408" lengthAdjust="spacingAndGlyphs">ROSA 0467 213 905</text>
      <text class="contact-line contact-mavis" x="50" y="438" textLength="396" lengthAdjust="spacingAndGlyphs">MAVIS 0438104629</text>
      <text class="find-us" x="478" y="366" textLength="250" lengthAdjust="spacingAndGlyphs">Find us online:</text>
    </svg>
    <nav class="social-tags" aria-label="Social links">
      <span class="social-tag">Lumo</span>
      <span class="social-tag">Chatter</span>
      <span class="social-tag">Tacky</span>
    </nav>
  </main>
</body>
</html>
```